Business Card Design

Want something very unique. No business, just personal. The image I submitted is for inspiration only.

Target Market(s)

friends and new acquaintances

Industry/Entity Type

Business

Contact Information for Business Card

Mara Deltow
Piñon Ridge, NM
505-271-4906
maradeltow@quillbox.net

```html
<!DOCTYPE html>
<html lang="en">
<head>
<meta charset="utf-8">
<title>Mara Deltow — Business Card</title>
<link rel="stylesheet" href="https://fonts.googleapis.com/css2?family=Tinos&family=Caudex&display=swap">
<style>
  :root {
    --backdrop: #4a2e1f;
    --card-dark: #2b2827;
    --text-light: #ffffff;
    --photo-top: #b9b2a4;
    --photo-mid: #8f8a6e;
    --photo-bottom: #c9b48e;
    --chip: #3d6bb0;
  }
  * { margin: 0; padding: 0; box-sizing: border-box; }
  html, body {
    width: 1200px;
    height: 967px;
    overflow: hidden;
    background: var(--backdrop);
  }
  .card {
    position: absolute;
    left: 100px;
    top: 198px;
    width: 1000px;
    height: 572px;
    display: flex;
    box-shadow: 0 14px 30px rgba(0,0,0,0.45);
  }
  .card__photo {
    width: 400px;
    height: 100%;
    background: linear-gradient(180deg, var(--photo-top) 0%, var(--photo-mid) 45%, var(--photo-bottom) 100%);
  }
  .card__info {
    flex: 1;
    background: var(--card-dark);
    color: var(--text-light);
    position: relative;
    font-family: "Tinos", "Times New Roman", serif;
  }
  .card__name {
    position: absolute;
    left: 70px;
    top: 62px;
    font-size: 54px;
    font-weight: 400;
    letter-spacing: 1px;
    line-height: 1;
  }
  .card__role {
    position: absolute;
    left: 70px;
    top: 126px;
    font-family: "Caudex", Georgia, serif;
    font-size: 29px;
    letter-spacing: 1px;
  }
  .contact {
    position: absolute;
    left: 0;
    right: 0;
    top: 222px;
    list-style: none;
    display: flex;
    flex-direction: column;
    align-items: center;
    gap: 22px;
    font-size: 31px;
  }
  .contact__item {
    display: flex;
    align-items: center;
    gap: 8px;
    line-height: 1;
  }
  .contact__icon { width: 28px; height: 28px; fill: var(--text-light); }
  .social {
    position: absolute;
    left: 0;
    right: 0;
    top: 462px;
    display: flex;
    justify-content: center;
    align-items: center;
    gap: 16px;
    font-size: 28px;
    letter-spacing: 1px;
  }
  .social__links { display: flex; gap: 12px; list-style: none; }
  .social__link { display: flex; align-items: center; gap: 5px; font-size: 20px; }
  .social__chip { width: 14px; height: 14px; background: var(--chip); border-radius: 3px; }
</style>
</head>
<body>
  <article class="card">
    <div class="card__photo" role="img" aria-label="Photo of the card owner crouching beside resting cheetahs at a wildlife enclosure"></div>
    <section class="card__info">
      <h1 class="card__name">MARA DELTOW</h1>
      <p class="card__role">Animal Lover &amp; Care Taker</p>
      <ul class="contact">
        <li class="contact__item">
          <svg class="contact__icon" viewBox="0 0 24 24" aria-hidden="true"><path d="M12 2a7 7 0 0 0-7 7c0 5 7 13 7 13s7-8 7-13a7 7 0 0 0-7-7zm0 9.5A2.5 2.5 0 1 1 12 6.5a2.5 2.5 0 0 1 0 5z"/></svg>
          Piñon Ridge, NM
        </li>
        <li class="contact__item">
          <svg class="contact__icon" viewBox="0 0 24 24" aria-hidden="true"><path d="M6.6 10.8a15 15 0 0 0 6.6 6.6l2.2-2.2a1 1 0 0 1 1-.25 11.4 11.4 0 0 0 3.6.57 1 1 0 0 1 1 1V20a1 1 0 0 1-1 1A17 17 0 0 1 3 4a1 1 0 0 1 1-1h3.5a1 1 0 0 1 1 1c0 1.25.2 2.450.57 3.57a1 1 0 0 1-.25 1z"/></svg>
          505-271-4906
        </li>
        <li class="contact__item">
          <svg class="contact__icon" viewBox="0 0 24 24" aria-hidden="true"><path d="M3 9l9-6 9 6v11H3zm2 1.2V18h14v-7.8l-7 4.6z"/></svg>
          maradeltow@quillbox.net
        </li>
      </ul>
      <div class="social">
        <span class="social__label">Follow Us On</span>
        <ul class="social__links">
          <li class="social__link"><span class="social__chip"></span>Friendly</li>
          <li class="social__link"><span class="social__chip"></span>Chirpa</li>
          <li class="social__link"><span class="social__chip"></span>Workring</li>
        </ul>
      </div>
    </section>
  </article>
</body>
</html>
```